Technology Project Portal - Project Listing portal

We require a logo & website designed for our new project.

Project Name: lumrik
Description:
We have a webapp where clients and service providers can come, signup and register development projects. Service providers can the browse projects and contact clients via the portal

Design brief:
Clean & Modern - See Attached color palet & style references. (Feel free to try alternative color palets)

See Project Proposal for site requirements.
UX flow section details pages requires

Examples of all standard UI Components required e.g.
text box / field
Drop down
date picker
etc..
Updates

Target Market(s)

Business / Technology providers

Logo Text

LumRik

Coding

Coded - Design and coding required

Number of Pages Required

5+ page

Requirements
Must have
• Clean Modern Design
Examples for all common UI elements
Templates for common Web App Dialogs e.g. Confirm Delete/Logout etc

```html
<!DOCTYPE html>
<html lang="en">
<head>
<meta charset="utf-8">
<title>LumRik – My Projects</title>
<link rel="stylesheet" href="https://fonts.googleapis.com/css2?family=Roboto:wght@300;400;500&display=swap">
<style>
:root{
  --coral:#fb876a;
  --coral-soft:#fde3dc;
  --ink:#1f1f24;
  --muted:#7d7f86;
  --light:#9a9ca3;
  --line:#e8e9ec;
  --page:#f4f5f7;
  --white:#ffffff;
  --chip:#f1f2f4;
}
*{box-sizing:border-box;margin:0;padding:0}
html,body{width:1200px;height:872px;overflow:hidden}
body{font-family:'Roboto',Arial,sans-serif;background:var(--page);color:var(--ink);position:relative;letter-spacing:.2px}
.sidebar{position:absolute;left:0;top:0;width:208px;height:872px;background:var(--white)}
.brand{position:absolute;left:32px;top:12px;font-size:36px;font-weight:500;color:var(--coral);letter-spacing:1px}
.nav{list-style:none;position:absolute;top:78px;left:0;width:208px}
.nav li{position:relative;height:38.4px;display:flex;align-items:center;padding-left:34px;font-size:11.5px;color:var(--muted)}
.nav li svg{width:16px;height:16px;margin-right:13px;flex:none}
.nav li.active{color:var(--ink)}
.nav li.active::before{content:"";position:absolute;left:0;top:0;width:2px;height:100%;background:var(--coral)}
.copyright{position:absolute;left:32px;top:816px;font-size:11px;color:var(--muted)}
.crumb{position:absolute;left:242px;top:24px;font-size:11.5px;color:var(--muted)}
.create-btn{position:absolute;left:754px;top:13px;width:168px;height:38px;border:1px solid var(--coral);border-radius:19px;display:flex;align-items:center;padding-left:5px;font-size:11.5px;color:var(--ink);background:transparent}
.create-btn .plus{width:27px;height:27px;border-radius:50%;background:var(--coral);margin-right:10px;display:flex;align-items:center;justify-content:center}
.bell{position:absolute;left:1048px;top:22px}
.avatar{position:absolute;left:1130px;top:13px;width:38px;height:38px;border-radius:50%;background:linear-gradient(135deg,#8b6a55,#c9a48a);box-shadow:0 2px 6px rgba(0,0,0,.2)}
.page-head{position:absolute;left:240px;top:78px;width:928px;height:30px;display:flex;align-items:center}
.page-head h1{font-size:24px;font-weight:400}
.page-head .dot{width:3px;height:3px;border-radius:50%;background:var(--muted);margin:0 16px 0 19px}
.page-head .total{font-size:11.5px;color:var(--muted)}
.page-head .sort{margin-left:auto;font-size:11.5px;color:var(--muted);display:flex;align-items:center;gap:4px}
.page-head .sort b{font-weight:400;color:var(--ink)}
.divider{position:absolute;left:240px;top:128px;width:928px;height:1px;background:var(--line)}
.card{position:absolute;left:240px;width:928px;height:200px;background:var(--white);border-radius:3px;overflow:hidden}
.card .thumb{position:absolute;left:0;top:0;width:220px;height:200px;background:linear-gradient(135deg,#0d4a32 0%,#1f8a5a 40%,#0f5c3c 70%,#2aa36a 100%)}
.card h2{position:absolute;left:236px;top:172px;font-size:16.5px;font-weight:400}
.card h2{top:28px}
.card p{position:absolute;left:236px;top:55px;width:640px;font-size:11.2px;line-height:17.6px;color:var(--muted);font-weight:300}
.card .rule{position:absolute;left:236px;right:16px;top:129px;height:1px;background:var(--line)}
.card .meta{position:absolute;left:236px;top:152px;display:flex;align-items:center;font-size:11.5px;color:var(--muted)}
.card .meta .chip{width:27px;height:27px;border-radius:50%;background:var(--chip);display:flex;align-items:center;justify-content:center;margin-right:8px}
.card .meta .gap{width:26px}
.card .view-btn{position:absolute;right:16px;top:146px;width:176px;height:38px;border-radius:19px;background:var(--coral);color:var(--white);font-size:11.5px;display:flex;align-items:center;justify-content:center}
.card .edit{position:absolute;right:16px;top:16px;width:27px;height:27px;border-radius:50%;border:1px solid var(--coral);display:flex;align-items:center;justify-content:center}
.loading{position:absolute;left:632px;top:814px;display:flex;align-items:center;font-size:11.5px;color:var(--muted)}
.loading svg{margin-right:14px}
</style>
</head>
<body>
<aside class="sidebar">
  <div class="brand">LumRik</div>
  <ul class="nav">
    <li class="active"><svg viewBox="0 0 16 16" fill="none" stroke="#fb876a" stroke-width="1.3"><path d="M8 3 2 6l6 3 6-3z"/><path d="M2 8.5l6 3 6-3"/><path d="M2 11l6 3 6-3"/></svg>My Projects</li>
    <li><svg viewBox="0 0 16 16" fill="none" stroke="#7d7f86" stroke-width="1.2"><path d="M4 11V7a4 4 0 0 1 8 0v4l1.5 1.5h-11z"/><path d="M7 14h2"/></svg>Notification</li>
    <li><svg viewBox="0 0 16 16" fill="none" stroke="#7d7f86" stroke-width="1.2"><circle cx="7" cy="5" r="3"/><path d="M2 14c0-3 2-5 5-5"/><circle cx="12" cy="12" r="1.6"/></svg>My Profile</li>
    <li><svg viewBox="0 0 16 16" fill="none" stroke="#7d7f86" stroke-width="1.2"><path d="M8 1v14"/><path d="M11 4.5C10.5 3.5 9.5 3 8 3 6 3 5 4 5 5.3 5 8 11 7 11 10.5 11 12 9.8 13 8 13c-1.7 0-2.8-.6-3.3-1.7"/></svg>Payment Details</li>
  </ul>
  <div class="copyright">© 2020 LumRik</div>
</aside>

<div class="crumb">My Projects</div>
<div class="create-btn"><span class="plus"><svg width="13" height="13" viewBox="0 0 13 13" stroke="#fff" stroke-width="1.4"><path d="M6.5 1v11M1 6.5h11"/></svg></span>Create New Projects</div>
<svg class="bell" width="18" height="20" viewBox="0 0 18 20" fill="none" stroke="#7d7f86" stroke-width="1.2"><path d="M4 14V9a5 5 0 0 1 10 0v5l1.5 1.5h-13z"/><path d="M7.5 18h3"/><circle cx="14.5" cy="3.5" r="2" fill="#fb876a" stroke="none"/></svg>
<div class="avatar" role="img" aria-label="User profile photo"></div>

<div class="page-head">
  <h1>Active Projects</h1><span class="dot"></span><span class="total">24 Total</span>
  <span class="sort">Shorted by: <b>Active</b><svg width="10" height="6" viewBox="0 0 10 6" fill="none" stroke="#1f1f24" stroke-width="1.1"><path d="M1 1l4 4 4-4"/></svg></span>
</div>
<div class="divider"></div>

<article class="card" style="top:144px">
  <div class="thumb" role="img" aria-label="Project cover photo of tropical green leaves"></div>
  <h2>Lorem Ipsum is simply dummy title consectetur adipiscing</h2>
  <p>sed do eiusmod tempor incididunt ut labore et dolore magna aliqua. Ut enim ad minim veniam, quis nostrud exercitation ullamco laboris nisi ut aliquip ex ea commodo consequat. Duis aute irure dolor ...</p>
  <span class="edit"><svg width="12" height="12" viewBox="0 0 12 12" fill="none" stroke="#fb876a" stroke-width="1"><path d="M6 2H2v8h8V6"/><path d="M5 7l.3-1.7L10 .8l1.2 1.2-4.5 4.7z"/></svg></span>
  <div class="rule"></div>
  <div class="meta"><span class="chip"><svg width="13" height="9" viewBox="0 0 13 9" fill="none" stroke="#6a6c72" stroke-width="1.1"><path d="M1 4.5C3 1.5 10 1.5 12 4.5 10 7.5 3 7.5 1 4.5z"/><circle cx="6.5" cy="4.5" r="1.5" fill="#6a6c72"/></svg></span>24.Project Views<span class="gap"></span><span class="chip"><svg width="10" height="11" viewBox="0 0 10 11" fill="none" stroke="#6a6c72" stroke-width="1.1"><circle cx="5" cy="3" r="2.2"/><path d="M1 10.5c0-2.5 1.8-4 4-4s4 1.5 4 4"/></svg></span>13.Contacts</div>
  <span class="view-btn">View Project Detail</span>
</article>

<article class="card" style="top:360px">
  <div class="thumb" role="img" aria-label="Project cover photo of tropical green leaves"></div>
  <h2>Lorem Ipsum is simply dummy title consectetur adipiscing</h2>
  <p>sed do eiusmod tempor incididunt ut labore et dolore magna aliqua. Ut enim ad minim veniam, quis nostrud exercitation ullamco laboris nisi ut aliquip ex ea commodo consequat. Duis aute irure dolor ...</p>
  <span class="edit"><svg width="12" height="12" viewBox="0 0 12 12" fill="none" stroke="#fb876a" stroke-width="1"><path d="M6 2H2v8h8V6"/><path d="M5 7l.3-1.7L10 .8l1.2 1.2-4.5 4.7z"/></svg></span>
  <div class="rule"></div>
  <div class="meta"><span class="chip"><svg width="13" height="9" viewBox="0 0 13 9" fill="none" stroke="#6a6c72" stroke-width="1.1"><path d="M1 4.5C3 1.5 10 1.5 12 4.5 10 7.5 3 7.5 1 4.5z"/><circle cx="6.5" cy="4.5" r="1.5" fill="#6a6c72"/></svg></span>24.Project Views<span class="gap"></span><span class="chip"><svg width="10" height="11" viewBox="0 0 10 11" fill="none" stroke="#6a6c72" stroke-width="1.1"><circle cx="5" cy="3" r="2.2"/><path d="M1 10.5c0-2.5 1.8-4 4-4s4 1.5 4 4"/></svg></span>13.Contacts</div>
  <span class="view-btn">View Project Detail</span>
</article>

<article class="card" style="top:576px">
  <div class="thumb" role="img" aria-label="Project cover photo of tropical green leaves"></div>
  <h2>Lorem Ipsum is simply dummy title consectetur adipiscing</h2>
  <p>sed do eiusmod tempor incididunt ut labore et dolore magna aliqua. Ut enim ad minim veniam, quis nostrud exercitation ullamco laboris nisi ut aliquip ex ea commodo consequat. Duis aute irure dolor ...</p>
  <span class="edit"><svg width="12" height="12" viewBox="0 0 12 12" fill="none" stroke="#fb876a" stroke-width="1"><path d="M6 2H2v8h8V6"/><path d="M5 7l.3-1.7L10 .8l1.2 1.2-4.5 4.7z"/></svg></span>
  <div class="rule"></div>
  <div class="meta"><span class="chip"><svg width="13" height="9" viewBox="0 0 13 9" fill="none" stroke="#6a6c72" stroke-width="1.1"><path d="M1 4.5C3 1.5 10 1.5 12 4.5 10 7.5 3 7.5 1 4.5z"/><circle cx="6.5" cy="4.5" r="1.5" fill="#6a6c72"/></svg></span>24.Project Views<span class="gap"></span><span class="chip"><svg width="10" height="11" viewBox="0 0 10 11" fill="none" stroke="#6a6c72" stroke-width="1.1"><circle cx="5" cy="3" r="2.2"/><path d="M1 10.5c0-2.5 1.8-4 4-4s4 1.5 4 4"/></svg></span>13.Contacts</div>
  <span class="view-btn">View Project Detail</span>
</article>

<div class="loading"><svg width="18" height="18" viewBox="0 0 18 18" fill="none" stroke-width="2"><circle cx="9" cy="9" r="7" stroke="var(--coral-soft)"/><path d="M9 2a7 7 0 0 0-5 11.9" stroke="#fb876a" stroke-linecap="round"/></svg>Loading more results</div>
</body>
</html>
```